Webdesign für B2B-Unternehmen
Zielgruppe
Wir sind im B2B Geschäft tätig und sind ein Spin Off der Firma www.plimora.com
Aufgabenstellung
Es soll sehr Übersichtlich und nicht zu verspielt sein. Unsere Potenziellen Kunden sollen sehr einfach und schnell an Ihr Ziel kommen

```html
<!DOCTYPE html>
<html lang="de">
<head>
<meta charset="utf-8">
<title>Velorna – IT-Solutions</title>
<link href="https://fonts.googleapis.com/css2?family=Roboto:wght@400;500;700&family=Noto+Sans:wght@400;500;700&display=swap" rel="stylesheet">
<style>
:root{
  --navy:#0b2440;
  --navy-deep:#061a30;
  --navy-mid:#08345a;
  --mint:#84efa6;
  --mint-dark:#4fd08a;
  --white:#ffffff;
  --ink:#0a2238;
}
*{margin:0;padding:0;box-sizing:border-box}
html,body{width:1200px;height:2376px;overflow:hidden}
body{position:relative;background:var(--navy);font-family:"Noto Sans",sans-serif;color:var(--white)}
.abs{position:absolute}
a{color:inherit}

/* hero */
.hero-art{left:0;top:0;width:1200px;height:664px;
  background:
   radial-gradient(ellipse 520px 130px at 600px 560px,rgba(132,239,166,.55),transparent 70%),
   radial-gradient(ellipse 300px 90px at 820px 440px,rgba(132,239,166,.45),transparent 70%),
   radial-gradient(ellipse 260px 80px at 150px 570px,rgba(132,239,166,.35),transparent 70%),
   linear-gradient(180deg,#062038 0%,#07294a 45%,#0d4a5a 78%,#1c7a6a 100%);}
.hero-band{left:0;top:664px;width:1200px;height:13px;background:var(--mint)}
.nav a{position:absolute;top:44px;font-size:15px;text-decoration:underline}
.brand{position:absolute;font-family:"Roboto",sans-serif;font-weight:400;letter-spacing:6px;text-transform:uppercase}
.brand-top{left:548px;top:40px;font-size:19px;width:106px;text-align:center}
.contact-btn{left:956px;top:39px;width:88px;height:27px;border-radius:4px;background:var(--mint);color:var(--ink);
  font-family:"Roboto",sans-serif;font-weight:700;font-size:16px;text-align:center;line-height:27px;text-decoration:none}
.hero-title{left:0;width:1200px;top:278px;text-align:center;font-family:"Roboto",sans-serif;font-weight:700;font-size:66px}
.hero-sub{left:0;width:1200px;top:358px;text-align:center;font-size:29px}

/* services */
.services{left:0;top:677px;width:1200px;height:671px;
  background:radial-gradient(ellipse 700px 500px at 1000px 350px,#0b4a72 0%,transparent 70%),linear-gradient(180deg,#0a2a4a,#0a3556)}
.sec-title{left:167px;top:773px;font-family:"Roboto",sans-serif;font-weight:700;font-size:56px}
.sec-sub{left:167px;top:836px;font-size:25px}
.card{position:absolute;border:2px solid var(--white);border-radius:3px;background:var(--navy-deep);text-align:center;padding:0 10px}
.card h3{font-weight:400;font-size:20px;margin-top:22px}
.card p{font-size:11px;line-height:17px;margin-top:12px}
.card .more{display:inline-block;width:88px;height:28px;line-height:28px;border-radius:3px;background:var(--white);color:var(--ink);
  font-family:"Roboto",sans-serif;font-weight:700;font-size:17px;margin-top:20px}
.card-left{left:169px;top:970px;width:218px;height:218px}
.card-right{left:813px;top:970px;width:218px;height:218px}
.card-featured{left:472px;top:951px;width:255px;height:255px;border-color:var(--mint);padding:0 14px}
.card-featured h3{font-size:22px;margin-top:26px}
.card-featured p{font-size:12px;line-height:19px}
.card-featured .more{background:var(--mint);margin-top:18px}
.social-side{left:1125px;width:44px;height:44px;border-radius:50%;background:var(--white);z-index:5}

/* feature */
.feature-photo{left:0;top:1348px;width:1200px;height:692px;
  background:radial-gradient(ellipse 380px 520px at 260px 380px,#3f8c6a 0%,transparent 75%),linear-gradient(90deg,#2f7358 0%,#1c5546 50%,#0f3e36 100%)}
.feature-text{right:167px;text-align:right}
.feature-title{top:1482px;font-family:"Roboto",sans-serif;font-weight:700;font-size:56px}
.feature-sub{top:1544px;font-size:25px}
.feature-list{top:1615px;font-size:25px;line-height:38px;list-style:none}
.btn{position:absolute;top:1815px;height:48px;border-radius:4px;background:var(--navy-deep);border-right:3px solid var(--mint);border-bottom:3px solid var(--mint);
  font-family:"Roboto",sans-serif;font-weight:700;font-size:24px;text-align:center;line-height:46px}
.btn-info{left:694px;width:160px}
.btn-buy{left:890px;width:138px}

/* footer */
.footer{left:0;top:2040px;width:1200px;height:336px;background:var(--mint);color:var(--ink)}
.brand-foot{left:115px;top:2100px;font-size:30px;color:var(--ink)}
.copyright{left:139px;top:2175px;font-family:"Roboto",sans-serif;font-weight:500;font-size:11px;color:var(--ink)}
.privacy{left:139px;top:2214px;font-family:"Roboto",sans-serif;font-weight:500;font-size:11px;color:var(--ink);text-decoration:underline}
.foot-social{top:2256px;width:24px;height:24px;border-radius:50%;background:var(--ink)}
.foot-links{right:312px;top:2100px;text-align:right;list-style:none;font-family:"Roboto",sans-serif;font-weight:700;font-size:16px;line-height:31px;color:var(--ink)}
.foot-links a{text-decoration:underline}
.divider{left:917px;top:2098px;width:2px;height:198px;background:var(--ink)}
.visit{left:941px;color:var(--ink)}
.visit h4{font-family:"Roboto",sans-serif;font-weight:700;font-size:16px}
.visit p{font-size:16px;line-height:17px;margin-top:12px}
</style>
</head>
<body>

<div class="abs hero-art" role="img" aria-label="Abstrakte grüne Datenlandschaft mit leuchtenden Punktlinien auf dunkelblauem Grund"></div>
<div class="abs hero-band"></div>

<nav class="nav">
  <a style="left:139px">Banking</a>
  <a style="left:289px">Digital Identity &amp; Security</a>
  <a style="left:735px">IoT</a>
  <a style="left:843px">SIM</a>
</nav>
<div class="brand brand-top">Velorna</div>
<a class="abs contact-btn">Contact</a>

<h1 class="abs hero-title">Lorem Ipsum</h1>
<p class="abs hero-sub">We are your partner for IT-Solutions!</p>

<section class="abs services"></section>
<h2 class="abs sec-title">Lorem Ipsum</h2>
<p class="abs sec-sub">We are your partner for IT-Solutions!</p>

<div class="card card-left">
  <h3>Lorem Ipsum</h3>
  <p>Lorem ipsum dolor sit amet, consectetur adipiscing elit, sed do eiusmod tempor incididunt ut labore et dolore magna aliqua. Quis ipsum suspendisse ultrices gravida.</p>
  <span class="more">More</span>
</div>
<div class="card card-featured">
  <h3>Lorem Ipsum</h3>
  <p>Lorem ipsum dolor sit amet, consectetur adipiscing elit, sed do eiusmod tempor incididunt ut labore et dolore magna aliqua. Quis ipsum suspendisse ultrices gravida. Risus commodo viverra maecenas.</p>
  <span class="more">More</span>
</div>
<div class="card card-right">
  <h3>Lorem Ipsum</h3>
  <p>Lorem ipsum dolor sit amet, consectetur adipiscing elit, sed do eiusmod tempor incididunt ut labore et dolore magna aliqua. Quis ipsum suspendisse ultrices gravida.</p>
  <span class="more">More</span>
</div>

<div class="abs feature-photo" role="img" aria-label="Foto einer Frau, die in der Bahn auf ihr Smartphone schaut, grün eingefärbt"></div>

<span class="abs social-side" style="top:1188px" aria-label="Social-Media-Link"></span>
<span class="abs social-side" style="top:1265px" aria-label="Video-Kanal"></span>
<span class="abs social-side" style="top:1342px" aria-label="Social-Media-Link"></span>

<h2 class="abs feature-text feature-title">Lorem Ipsum dolor sit</h2>
<p class="abs feature-text feature-sub">We are your partner for IT-Solutions!</p>
<ul class="abs feature-text feature-list">
  <li>Et dolore magna</li>
  <li>Suspendisse ultrices</li>
  <li>consectetur adipiscing</li>
  <li>Incidunt ut labore</li>
</ul>
<a class="btn btn-info">More info...</a>
<a class="btn btn-buy">Buy now!</a>

<footer class="abs footer"></footer>
<div class="brand brand-foot">Velorna</div>
<p class="abs copyright">© 2020 All Rights reserved, Velorna GmbH</p>
<a class="abs privacy">Privacy Policy</a>
<span class="abs foot-social" style="left:139px"></span>
<span class="abs foot-social" style="left:174px"></span>
<span class="abs foot-social" style="left:209px"></span>

<ul class="abs foot-links">
  <li><a>IoT</a></li>
  <li><a>SIM</a></li>
  <li><a>Banking</a></li>
  <li><a>Digital Identity &amp; Security</a></li>
  <li><a>About us</a></li>
</ul>
<div class="abs divider"></div>
<div class="abs visit" style="top:2102px">
  <h4>Visit Us</h4>
  <p>Musterstraße 25<br>Musterstadt, 54021</p>
</div>
<div class="abs visit" style="top:2196px">
  <h4>Or Call Us...</h4>
  <p>01547 20391876</p>
</div>

</body>
</html>
```